Web Design Project

Full website, similar _function_ to http://www.kindlarkfund.com/
You can not only make charities, but also communicate social or environmental problems by posting them on the website.
I need a full layout design, right now I am using a slightly changed bootstrap. View attached file "basic css" for current containers layout
Including front page, static text page (SEO), show listing page and content page, all the same look and feel. Dont focus to hard on the charity part...

Logo will be needed:
The URL - also the Logo - is Wutbrand.de - that is German for "Outcry" - so working with a "!" makes prob. sense, like Wutbrand!de or so... (EXTRA)

Colour Scheme:
I do not have a colour scheme, but I alreay think "Red URL with green elements" would be nice - that means please give me some other ideas ... I am not a designer, right?! :)

NO CODING NEEDED

Reason: I just got too few designs, some nice with it, though - I will clarify my needs new so it will be easier to reply with suggestions! :)

Target Market(s)

People who want to do charity and help other people

Industry/Entity Type

Charity

Requirements
Must have
• responsive design (tablet, smartphone)
static frame header (like here at pixelhive)

```html
<!DOCTYPE html>
<html lang="en">
<head>
<meta charset="utf-8">
<title>Wutbrand – Charity</title>
<link href="https://fonts.googleapis.com/css2?family=Source+Sans+3:ital,wght@0,400;0,600;0,700;1,400&family=Roboto+Condensed:wght@400&display=swap" rel="stylesheet">
<style>
:root{
  --red:#821a1e;
  --red-btn:#8c1b20;
  --red-head:#a3262b;
  --green:#6f9a1c;
  --green-light:#8dbb2b;
  --green-text:#7ba428;
  --paper:#f0ede6;
  --white:#ffffff;
  --text:#3a3a3a;
  --muted:#8a8a8a;
  --topbar:#5b5b5b;
  --line:#dcd8cf;
}
*{box-sizing:border-box;margin:0;padding:0}
html,body{width:1200px;height:1147px;overflow:hidden;background:var(--paper)}
body{font-family:"Source Sans 3",sans-serif;color:var(--text)}
.page{position:relative;width:1400px;height:1338px;transform:scale(.857143);transform-origin:0 0;background:var(--paper)}
.abs{position:absolute}

/* top bar */
.topbar{left:0;top:0;width:1400px;height:52px;background:var(--topbar);color:#fff;font-size:13px}
.topnav{left:317px;top:18px;display:flex;gap:0;white-space:nowrap}
.topnav span{margin-right:25px}
.topnav .sep{margin-right:25px;opacity:.8}
.lang-label{left:993px;top:20px;font-size:12px}
.lang{left:1089px;top:13px;width:99px;height:27px;background:#fff;border-radius:3px;color:#333;font-size:12px;display:flex;align-items:center;padding-left:9px;gap:8px}
.flag{width:18px;height:12px;background:#3b4f8f}

/* header */
.header{left:0;top:52px;width:1400px;height:104px;background:#f4f1eb}
.logo{left:218px;top:62px;display:flex;align-items:center;gap:14px;height:84px}
.logo-dot{width:30px;height:30px;border-radius:50%;background:var(--green)}
.logo-name{font-size:38px;font-weight:700;color:var(--green-text)}
.search-label{left:596px;top:104px;font-size:12px;color:#666}
.search{left:640px;top:98px;width:261px;height:26px;background:#fff;border:1px solid #d6d2c9;border-radius:2px}
.search svg{position:absolute;right:8px;top:4px}
.hbtn{top:86px;width:130px;height:40px;background:var(--red-btn);color:#fff;font-size:15px;display:flex;align-items:center;padding-left:22px;border-radius:2px;box-shadow:inset 0 -2px 0 rgba(0,0,0,.2)}
.hbtn .chev{position:absolute;right:14px;top:13px;width:14px;height:14px;border-radius:50%;background:#fff}

/* hero */
.band{left:0;top:156px;width:1400px;height:404px;background:var(--red)}
.hero{left:210px;top:156px;width:980px;height:404px;background:#fff;padding:0 3px 3px}
.hero-photo{width:100%;height:100%;background:linear-gradient(120deg,#6f5a3d 0%,#c8a37a 30%,#a98a5e 50%,#d9b896 70%,#5e4a37 100%)}
.hero-title{left:234px;top:438px;font-family:"Roboto Condensed",sans-serif;font-size:38px;color:#111;line-height:1}
.hero-sub{left:234px;top:480px;font-family:"Roboto Condensed",sans-serif;font-size:24px;color:#1a1a1a}
.dots{left:1113px;top:538px;display:flex;gap:3px}
.dots i{width:10px;height:10px;background:rgba(255,255,255,.45)}
.dots i:first-child{background:#fff}

/* breadcrumb */
.crumbs{left:210px;top:577px;width:980px;height:31px;background:#fff;font-size:12px;display:flex;align-items:center;padding-left:21px;gap:0}
.crumbs .home{color:var(--red)}
.crumbs .arr{color:var(--red);margin:0 26px 0 6px;font-size:10px}

/* feature boxes */
.box{top:628px;width:226px;height:157px;background:#fff}
.box h3{height:29px;background:linear-gradient(#b0343a,var(--red-btn));color:#fff;font-weight:400;font-size:16px;padding:4px 0 0 15px}
.box p{font-size:11px;line-height:18px;padding:12px 0 0 17px;color:#333}
.gbtn{position:absolute;background:linear-gradient(var(--green-light),var(--green));color:#fff;border:1px solid #5d8316;display:flex;align-items:center;justify-content:center;border-radius:2px}
.field{position:absolute;left:13px;top:110px;width:160px;height:27px;border:1px solid #d0ccc3;font-size:12px;color:#999;padding:6px 12px}

.divider{left:210px;top:803px;width:980px;height:1px;background:var(--line)}

/* welcome */
.welcome{left:213px;top:823px;font-size:24px;color:#555}
.welcome em{font-style:normal;color:var(--red)}
.welcome-photo{left:210px;top:866px;width:236px;height:104px;border:3px solid #ddd6cb;background:linear-gradient(90deg,#6b5c4c,#cfd3d4 45%,#9ba7b2 80%,#2e3947)}
.welcome-text{left:470px;top:864px;width:725px;font-size:11px;line-height:18px;color:#333}
.welcome-text p{margin-bottom:18px}

/* categories */
.cats{left:210px;top:1009px;width:226px;height:204px;background:#fff}
.cats h3{height:30px;background:linear-gradient(#9bc243,var(--green));color:#fff;font-weight:400;font-size:16px;padding:4px 0 0 15px}
.cats ul{list-style:none;padding:0 10px 0 12px}
.cats li{font-size:11px;height:33px;display:flex;align-items:center;gap:8px;border-bottom:1px solid #ddd;padding-left:2px}
.cats li:last-child{border:0}
.cats li b{color:var(--red);font-size:9px;font-weight:400}

/* blog */
.blog-head{left:460px;top:1010px;width:730px;height:31px;background:#fff}
.blog-head h2{position:absolute;left:11px;top:3px;font-size:20px;font-weight:400;color:var(--red)}
.nav-dot{position:absolute;top:8px;width:16px;height:16px;border-radius:50%;background:var(--green)}
.nav-dot svg{position:absolute;left:4px;top:4px}
.post{top:1060px;width:330px}
.quote{position:absolute;font-size:30px;color:#cfc9bd;font-family:Georgia,serif;line-height:1}
.post h4{position:absolute;left:25px;top:10px;font-size:14px;font-weight:400;color:var(--green-text)}
.post p{position:absolute;left:25px;top:34px;width:295px;font-size:11px;line-height:18px;color:#666}
.avatar{position:absolute;left:10px;top:100px;width:80px;height:57px;border:2px solid #ddd6cb}
.author{position:absolute;left:107px;top:108px;font-size:14px;color:var(--red)}
.role{position:absolute;left:107px;top:128px;font-size:12px;font-style:italic;color:var(--muted)}
.vsep{left:822px;top:1060px;width:0;height:152px;border-left:1px dashed #ccc}

/* footer */
.footer{left:0;top:1249px;width:1400px;height:89px;background:var(--red);color:#fff}
.fnav{position:absolute;left:211px;top:26px;font-size:11px;font-weight:600;white-space:nowrap}
.fnav span{margin-right:14px}
.fnav .sep{opacity:.8}
.copy{position:absolute;left:211px;top:46px;font-size:11px}
.copy em{font-style:normal;color:#9cc23d}
.follow{position:absolute;left:1038px;top:35px;font-size:12px}
.social{position:absolute;top:29px;width:26px;height:26px;border-radius:4px;background:#3d6fae}
</style>
</head>
<body>
<div class="page">

  <div class="abs topbar">
    <div class="abs topnav">
      <span>How KindLark works</span><span class="sep">|</span>
      <span>Charity membership</span><span class="sep">|</span>
      <span>Company fundraising</span><span class="sep">|</span>
      <span>Partnerships</span><span class="sep">|</span>
      <span>Help</span>
    </div>
    <div class="abs lang-label">Select Language :</div>
    <div class="abs lang"><span class="flag"></span>English
      <svg width="10" height="7" viewBox="0 0 10 7"><path d="M1 1l4 4 4-4" stroke="#333" stroke-width="1.6" fill="none"/></svg></div>
  </div>

  <div class="abs header"></div>
  <div class="abs logo"><span class="logo-dot"></span><span class="logo-name">Wutbrand</span></div>
  <div class="abs search-label">Search :</div>
  <div class="abs search"><svg width="20" height="16" viewBox="0 0 20 16"><circle cx="7" cy="6" r="5" stroke="#6f9a1c" stroke-width="2" fill="none"/><path d="M11 9l7 6" stroke="#6f9a1c" stroke-width="3"/></svg></div>
  <div class="abs hbtn" style="left:918px">Fundraising<span class="chev"></span></div>
  <div class="abs hbtn" style="left:1058px;padding-left:26px">Giving<span class="chev"></span></div>

  <div class="abs band"></div>
  <div class="abs hero"><div class="hero-photo" role="img" aria-label="Smiling young girl with her family, warm blurred background"></div></div>
  <div class="abs hero-title">People do the most amazing</div>
  <div class="abs hero-sub">things to raise money for the causes they love.</div>
  <div class="abs dots"><i></i><i></i><i></i><i></i><i></i></div>

  <div class="abs crumbs"><span class="home">Home</span><span class="arr">»</span><span>About Us</span><span class="arr">»</span><span>Charity</span></div>

  <div class="abs box" style="left:210px">
    <h3>Start fundraising</h3>
    <p>Step 1. Make your page<br>Step 2. Share it with your friends<br>Step 3. Raise money for your charity</p>
    <div class="gbtn" style="left:18px;top:110px;width:185px;height:31px;font-size:15px">Make your page</div>
  </div>
  <div class="abs box" style="left:461px">
    <h3>Donate to charity</h3>
    <p>Lorem Ipsum is simply dummy text of the<br>printing and typesetting industry.<br>Lorem Ipsum has been the industry's</p>
    <div class="field">Charity name</div>
    <div class="gbtn" style="left:178px;top:110px;width:35px;height:27px;font-size:15px">Go</div>
  </div>
  <div class="abs box" style="left:712px">
    <h3>Sponsor a friend</h3>
    <p>Lorem Ipsum is simply dummy text of the<br>printing and typesetting industry.<br>Lorem Ipsum has been the industry's</p>
    <div class="field">Friends name</div>
    <div class="gbtn" style="left:178px;top:110px;width:35px;height:27px;font-size:15px">Go</div>
  </div>
  <div class="abs box" style="left:964px">
    <h3>Become a charity member</h3>
    <p>Lorem Ipsum is simply dummy text of the<br>printing and typesetting industry.<br>Lorem Ipsum has been the industry's</p>
    <div class="gbtn" style="left:19px;top:110px;width:194px;height:27px;font-size:14px">About Charity Membership</div>
  </div>

  <div class="abs divider"></div>

  <div class="abs welcome">Welcome to <em>Wutbrand</em></div>
  <div class="abs welcome-photo" role="img" aria-label="Three smiling business people standing together"></div>
  <div class="abs welcome-text">
    <p>Lorem Ipsum is simply dummy text of the printing and typesetting industry. Lorem Ipsum has been the industry's standard dummy text ever since the 1500s, when an unknown printer took a galley of type and scrambled it to make a type specimen book. It has survived not only five centuries, but also the leap into electronic typesetting, remaining essentially unchanged. It was popularised in the 1960s with the release of Letraset sheets containing Lorem Ipsum passages, and more recently with desktop publishing software like Aldus PageMaker including versions of Lorem Ipsum.</p>
    <p>Lorem Ipsum is simply dummy text of the printing and typesetting industry. Lorem Ipsum has been the industry's standard dummy text ever since.</p>
  </div>

  <div class="abs cats">
    <h3>categories</h3>
    <ul>
      <li><b>»</b>Lorem Ipsum is simply dummy</li>
      <li><b>»</b>Lorem Ipsum is simply dummy</li>
      <li><b>»</b>Lorem Ipsum is simply dummy</li>
      <li><b>»</b>Lorem Ipsum is simply dummy</li>
      <li><b>»</b>Lorem Ipsum is simply dummy</li>
    </ul>
  </div>

  <div class="abs blog-head">
    <h2>Blog</h2>
    <span class="nav-dot" style="left:684px"><svg width="8" height="8" viewBox="0 0 8 8"><path d="M6 0L1 4l5 4z" fill="#fff"/></svg></span>
    <span class="nav-dot" style="left:704px"><svg width="8" height="8" viewBox="0 0 8 8"><path d="M2 0l5 4-5 4z" fill="#fff"/></svg></span>
  </div>

  <div class="abs post" style="left:470px">
    <span class="quote" style="left:0;top:0">“</span>
    <h4>Lorem Ipsum is simply dummy</h4>
    <p>Lorem Ipsum is simply dummy text of the printing and typeset-ting industry. Lorem Ipsum has been the industry's standard dummy text ever since the 1500s.</p>
    <span class="quote" style="left:318px;top:86px">”</span>
    <div class="avatar" role="img" aria-label="Elderly couple seen from behind at sunset" style="background:linear-gradient(#e89a3a,#a5561f)"></div>
    <div class="author">Milo Renner</div>
    <div class="role">Organiser</div>
  </div>
  <div class="abs vsep"></div>
  <div class="abs post" style="left:840px">
    <span class="quote" style="left:0;top:0">“</span>
    <h4>Lorem Ipsum is simply dummy</h4>
    <p>Lorem Ipsum is simply dummy text of the printing and typesetting industry. Lorem Ipsum has been the industry's standard dummy text ever since the 1500s.</p>
    <span class="quote" style="left:330px;top:86px">”</span>
    <div class="avatar" role="img" aria-label="Portrait of a smiling woman" style="background:linear-gradient(#e6e4df,#b89b84)"></div>
    <div class="author">Milo Renner</div>
    <div class="role">Organiser</div>
  </div>

  <div class="abs footer">
    <div class="fnav">
      <span>Home</span><span class="sep">|</span><span>About Us</span><span class="sep">|</span><span>How KindLark works</span><span class="sep">|</span><span>Charity membership</span><span class="sep">|</span><span>Company fundraising</span><span class="sep">|</span><span>Partnerships</span><span class="sep">|</span><span>Help</span>
    </div>
    <div class="copy">Copyright ©2013. <em>Wutbrand</em>&nbsp; All rights reserved.</div>
    <div class="follow">Follow Us :</div>
    <span class="social" style="left:1099px"></span>
    <span class="social" style="left:1130px;background:#4aa3d6"></span>
    <span class="social" style="left:1161px;background:#2f7bb5"></span>
  </div>

</div>
</body>
</html>
```